Coaching Workbook (for life & health coaching industry)

I created a coaching workbook using Canva. I would like it recreated more professionally in PowerPoint with better images and creative design using my 3 branding colors (teal primary, salmon secondary, and turquoise splash here and there).

Please use the attached image of lady sitting on dock at the lake on the first slide for the cover along with my logo and my titles (similar to my Canva version on my website).

My version of the workbook is attached. Thank you for turning my drab into fab:-) Merle Quistad, Life & Health Coach, Grief Recovery Specialist
Updates

To ensure clarity, I am looking for a PowerPoint (prefer vertical format) for a coaching manual FROM the material in the version that I created in Canva, which is currently on my website as a download at the bottom of my coaching page: https://brightmeadowguide.example/coaching-2 I will upload the pdf file as well as the example that I'm trying to recreate in PowerPoint, but more professionally and creatively. Thank You! Merle Quistad

Target Market(s)

My target audience is primarily female, with a few males each year, ages range from mid-twenties to sixties. Everyone will experience the pain of loss and grief. Women are more prone to reach out for help sooner.

Industry/Entity Type

Life Coaching

Font styles to use
Serif

Requirements
Must have
• Want it to feel personal, not corporate if that makes sense.
• Must use my 3 branding colors: HEX # 2994ae, 10dfd3, fa8070.
• Please use Playfair Display font for consistency with my website.
• The text for the workbook is included in the Word document attached below.
Should not have
• I'm not looking for the material on my website to be the focus of this workbook. I want the Canva version that I created to be converted more professionally and creatively in PowerPoint, so I can manage moving forward.

```html
<!DOCTYPE html>
<html lang="en">
<head>
<meta charset="utf-8">
<title>SMART Goals – Coaching Workbook</title>
<link rel="stylesheet" href="https://fonts.googleapis.com/css2?family=Playfair+Display:wght@400;700;900&display=swap">
<style>
  :root {
    --teal: #2994ae;
    --salmon: #fa8070;
    --turquoise: #10dfd3;
    --ink: #2b2b2b;
    --paper: #ffffff;
  }
  * { margin: 0; padding: 0; box-sizing: border-box; }
  html, body { width: 847px; height: 1200px; overflow: hidden; background: var(--paper); }
  .page {
    position: relative;
    width: 847px;
    height: 1200px;
    font-family: "Playfair Display", Georgia, serif;
    color: var(--ink);
    background: var(--paper);
  }
  .photo { position: absolute; }
  .photo--meal {
    left: 40px; top: 37px; width: 767px; height: 307px;
    background: linear-gradient(100deg, #c9a070 0%, #e3b46a 22%, #8a5a35 48%, #c08b55 68%, #dcd5cc 100%);
  }
  .photo--fitness {
    left: 37px; top: 361px; width: 376px; height: 307px;
    background: linear-gradient(135deg, #7fb7d8 0%, #2f6f9e 40%, #2aa0b4 65%, #c5a27a 100%);
  }
  .photo--promise {
    left: 431px; top: 361px; width: 376px; height: 307px;
    background: linear-gradient(160deg, #b9c2bd 0%, #a7b2ad 45%, #d9b8a4 70%, #aab4af 100%);
  }
  .title-badge {
    position: absolute;
    left: 234px; top: 321px; width: 379px; height: 84px;
    background: var(--salmon);
    color: var(--paper);
    display: flex; align-items: center; justify-content: center;
    font-size: 42px; font-weight: 700; letter-spacing: 3px;
  }
  .quote-band {
    position: absolute;
    left: 38px; top: 682px; width: 770px; height: 167px;
    background: var(--teal);
    color: var(--paper);
  }
  .quote-band__frame { position: absolute; left: 0; top: 0; }
  .quote-band__mark {
    position: absolute; left: 64px; top: -32px;
    font-size: 110px; font-weight: 900; line-height: 1;
  }
  .quote-band__text {
    position: absolute; left: 77px; top: 49px; width: 600px;
    font-size: 19px; line-height: 33px;
  }
  .quote-band__author {
    position: absolute; right: 91px; top: 113px;
    font-size: 17px; font-weight: 700;
  }
  .intro {
    position: absolute; left: 41px; top: 868px; width: 759px;
    font-size: 17px; line-height: 25px; text-align: justify;
  }
  .intro__term { color: var(--teal); letter-spacing: 4px; font-weight: 700; }
  .criteria { position: absolute; left: 41px; top: 926px; list-style: none; }
  .criteria li { height: 36.8px; font-size: 17px; line-height: 24px; }
  .criteria__word { font-size: 20px; }
  .criteria__initial { color: var(--teal); font-size: 21px; font-weight: 700; }
  .worksheet-note {
    position: absolute; left: 41px; top: 1122px;
    font-size: 17px; text-decoration: underline; text-decoration-thickness: 1px;
  }
  .worksheet-note span { text-decoration: none; display: inline-block; }
</style>
</head>
<body>
<main class="page">
  <div class="photo photo--meal" role="img" aria-label="Close-up of a burger beside a basket of fries and a cherry tomato"></div>
  <div class="photo photo--fitness" role="img" aria-label="Blue dumbbells, an exercise ball and running shoes"></div>
  <div class="photo photo--promise" role="img" aria-label="Two hands with linked little fingers making a promise"></div>

  <h1 class="title-badge">SMART Goals</h1>

  <blockquote class="quote-band">
    <svg class="quote-band__frame" width="770" height="167" viewBox="0 0 770 167" aria-hidden="true">
      <g fill="none" stroke="#ffffff" stroke-width="1">
        <polyline points="45,24 16,24 16,153 755,153 755,24 134,24"/>
        <line x1="68" y1="128" x2="542" y2="128" stroke-opacity="0.6"/>
      </g>
    </svg>
    <span class="quote-band__mark" aria-hidden="true">&#8221;</span>
    <p class="quote-band__text">There are no secrets to success. It is the result of preparation, hard work, and learning from failure."</p>
    <cite class="quote-band__author">Dorian Vale</cite>
  </blockquote>

  <p class="intro"><span class="intro__term">SMART goal</span> setting is a coaching methodology that provides structure to the process of formulating, planning, and achieving your goals. The acronym stands for:</p>

  <ul class="criteria">
    <li><span class="criteria__word"><span class="criteria__initial">S</span>pecific</span> - What exactly do you want to accomplish?</li>
    <li><span class="criteria__word"><span class="criteria__initial">M</span>easurable</span> - How will you track your progress to stay motivated?</li>
    <li><span class="criteria__word"><span class="criteria__initial">A</span>chievable</span> - How will you accomplish this goal?</li>
    <li><span class="criteria__word"><span class="criteria__initial">R</span>elevant</span> - Is this goal realistic given everything else on your plate?</li>
    <li><span class="criteria__word"><span class="criteria__initial">T</span>imely</span> - What is the target date for completion?</li>
  </ul>

  <p class="worksheet-note">This SMART Goal worksheet<span>&nbsp;can help you make changes to any area of your life.</span></p>
</main>
</body>
</html>
```